Health Coaching Flyer for New Clients

I need a two-sided flyer (3.5" x 8.5" preferred or 5" x 7") to distribute to potential coaching clients. My business name is Talvora Health & Wellness Coaching. My business is focused on helping people with habit changes that contribute to their overall well-being. I would like the design colors to be gender neutral. I would like a small photo of myself near the "my name is Jen" statement. Please feel free to change the logo color to match the design.

Target Market(s)

Adults of all ages.

Font styles to use
Serif

Requirements
Must have
• Emphasize my opening question (found in health coaching brochure - attached).
• Small picture of myself near "my name is Jen" statement.
Should not have
• No light of pastel colors.

```html
<!DOCTYPE html>
<html lang="en">
<head>
<meta charset="utf-8">
<title>Talvora Health &amp; Wellness Coaching – Flyer</title>
<link href="https://fonts.googleapis.com/css2?family=Open+Sans:ital,wght@0,400;0,600;0,700;0,800;1,600;1,700&display=swap" rel="stylesheet">
<style>
  :root{
    --page:#e9e9e9;
    --white:#ffffff;
    --ink:#1f1f1f;
    --dark-center:#6a6a6a;
    --dark-edge:#353535;
    --dark-top:#4a4a4a;
    --text-light:#ececec;
    --text-quote:#b9b9b9;
    --rule:#a9a9a9;
    --pill:#c9c9c9;
    --pill-shadow:#8d8d8d;
    --swoosh-grey:#9b9b9b;
    --meal-a:#e4e2dd;
    --meal-b:#bfc3bf;
    --meadow-a:#c3cfc4;
    --meadow-b:#93a275;
  }
  *{box-sizing:border-box;margin:0;padding:0}
  html,body{width:1130px;height:1200px;overflow:hidden}
  body{background:var(--page);font-family:"Open Sans",Arial,sans-serif;color:var(--text-light);position:relative}

  .flyer{position:absolute;top:30px;width:480px;height:1140px;overflow:hidden;
    background:radial-gradient(ellipse 75% 45% at 50% 60%,var(--dark-center),var(--dark-edge));
    box-shadow:0 4px 14px rgba(0,0,0,.25)}
  .flyer--front{left:60px}
  .flyer--back{left:590px}

  /* header */
  .brand{position:absolute;top:0;left:0;width:100%;height:140px;background:var(--white);
    display:flex;flex-direction:column;align-items:center;justify-content:center;gap:4px;color:var(--ink)}
  .brand__name{font-weight:800;font-size:52px;letter-spacing:4px;line-height:1}
  .brand__tag{font-weight:800;font-size:13px;letter-spacing:1.5px;line-height:1.4;text-transform:uppercase}

  /* photo placeholders */
  .photo{position:absolute;left:0;width:100%}
  .photo--meal{top:140px;height:480px;background:linear-gradient(180deg,var(--meal-a),var(--meal-b))}
  .photo--meadow{top:0;height:380px;background:linear-gradient(180deg,var(--meadow-a),var(--meadow-b))}
  .portrait{position:absolute;left:282px;top:500px;width:170px;height:170px;border-radius:50%;
    background:#8a6a5a;border:6px solid #d6d6d6;
    box-shadow:0 2px 6px rgba(0,0,0,.4);z-index:3}

  .swoosh{position:absolute;left:0;width:100%;height:100px;display:block;z-index:2}
  .swoosh--front{top:580px}
  .swoosh--back{top:320px}
  .foot-curve{position:absolute;left:0;bottom:0;width:100%;height:120px;display:block}

  /* dark content */
  .content{position:absolute;left:0;width:100%;padding:0 26px;z-index:2}
  .content--front{top:690px}
  .content--back{top:420px;padding:0 30px}

  .headline{font-weight:800;font-size:19px;line-height:1.4;text-align:center;text-transform:uppercase;color:var(--text-light)}
  .rule{height:1px;background:var(--rule);margin:12px 0 16px}
  .intro{font-size:14.5px;line-height:1.5;text-align:justify}
  .intro strong{display:block;font-weight:700}
  .quote{font-weight:700;font-style:italic;font-size:16px;line-height:1.4;text-align:center;color:var(--text-quote);margin-top:26px}
  .content--back .quote{margin-top:24px}

  .section-title{font-weight:700;font-size:19px;text-transform:uppercase;letter-spacing:.3px}
  .section-title + .rule{margin:10px 0 12px}
  .benefits{list-style:none}
  .benefits li{font-size:14.5px;line-height:1.45;padding-left:14px;position:relative;margin-bottom:10px}
  .benefits li::before{content:"•";position:absolute;left:0}
  .invite{font-size:14.5px;line-height:1.45;margin-top:22px}
  .offer{border:1.5px solid var(--rule);border-radius:10px;padding:10px 14px;margin-top:20px;
    text-align:center;font-weight:700;font-size:14.5px;line-height:1.4;color:var(--white)}

  /* footer */
  .phone{position:absolute;left:50%;top:1030px;transform:translateX(-50%);width:230px;height:40px;border-radius:20px;
    background:linear-gradient(180deg,#dcdcdc,var(--pill));box-shadow:0 3px 0 var(--pill-shadow);
    display:flex;align-items:center;justify-content:center;gap:10px;color:var(--ink);font-size:19px;z-index:3}
  .phone svg{width:20px;height:20px}
  .contact{position:absolute;left:0;bottom:18px;width:100%;text-align:center;color:var(--ink);font-size:15.5px;z-index:3}
</style>
</head>
<body>

<section class="flyer flyer--front">
  <header class="brand">
    <span class="brand__name">TALVORA</span>
    <span class="brand__tag">Health &amp; Wellness Coaching</span>
  </header>
  <div class="photo photo--meal" role="img" aria-label="Photo of a smiling woman eating a fresh salad at a kitchen table with juices and vegetables"></div>
  <svg class="swoosh swoosh--front" viewBox="0 0 480 100" preserveAspectRatio="none" aria-hidden="true">
    <path d="M0 40 Q240 95 480 20 L480 100 L0 100Z" fill="var(--swoosh-grey)"/>
    <path d="M0 50 Q240 100 480 30 L480 100 L0 100Z" fill="var(--white)"/>
    <path d="M0 64 Q240 112 480 46 L480 100 L0 100Z" fill="var(--dark-top)"/>
  </svg>
  <div class="portrait" role="img" aria-label="Small portrait photo of Jen, the coach"></div>

  <div class="content content--front">
    <h1 class="headline">Need support in making real, lasting lifestyle and behavior changes?</h1>
    <div class="rule"></div>
    <p class="intro"><strong>My name is Jen.</strong>I am studying to become an VITALA - Certified Functional Health Coach. My training involves many science-based practices that improve both our health and how we grow and change as humans. I now have the opportunity to turn that knowledge into practice by coaching actual clients interested in improving their own health and wellbeing.</p>
    <p class="quote">Please contact me. I’m ready to support you as you work to improve your health. - Jen Talvora</p>
  </div>

  <svg class="foot-curve" viewBox="0 0 480 120" preserveAspectRatio="none" aria-hidden="true">
    <path d="M0 52 Q240 20 480 52 L480 120 L0 120Z" fill="var(--swoosh-grey)"/>
    <path d="M0 60 Q240 30 480 60 L480 120 L0 120Z" fill="var(--white)"/>
  </svg>
  <div class="phone">
    <svg viewBox="0 0 20 20" aria-hidden="true"><circle cx="10" cy="10" r="8.5" fill="none" stroke="currentColor" stroke-width="1.5"/><path d="M7 5.5c.6-.3 1 0 1.3.6l.6 1.3c.2.5 0 .9-.4 1.2l-.4.3c.4 1 1.2 1.8 2.2 2.3l.3-.4c.3-.4.8-.6 1.2-.4l1.3.6c.6.3.8.8.5 1.3-.5 1-1.5 1.4-2.6 1-2.2-.8-3.9-2.5-4.7-4.7-.4-1.1 0-2.2.7-2.9z" fill="currentColor"/></svg>
    <span>555-210-4837</span>
  </div>
  <p class="contact">Please contact Jen Talvora: talvorahwc@mailbox.example</p>
</section>

<section class="flyer flyer--back">
  <div class="photo photo--meadow" role="img" aria-label="Photo of a woman with raised arms in a green meadow, with a heart of fruits and vegetables in the lower right corner"></div>
  <svg class="swoosh swoosh--back" viewBox="0 0 480 100" preserveAspectRatio="none" aria-hidden="true">
    <path d="M0 30 Q160 85 480 40 L480 100 L0 100Z" fill="var(--swoosh-grey)"/>
    <path d="M0 40 Q160 92 480 50 L480 100 L0 100Z" fill="var(--white)"/>
    <path d="M0 56 Q160 104 480 66 L480 100 L0 100Z" fill="var(--dark-top)"/>
  </svg>

  <div class="content content--back">
    <h2 class="section-title">Functional Health Coaches…</h2>
    <div class="rule"></div>
    <ul class="benefits">
      <li>Leverage your strengths rather than focus on your weaknesses</li>
      <li>Support you in finding your own strategies and motivation for change</li>
      <li>Provide a judgment-free zone and support your autonomy</li>
      <li>Use an experimental mindset to find and develop sustainable habits</li>
      <li>Act as your accountability partner as you reach your unique health goals; whether they be improving sleep, diet, fitness, social connection, or reducing stress.</li>
    </ul>
    <p class="invite">I would like to invite you to participate with me as a client as I continue to hone my coaching skills. We can develop a plan and schedule that aligns with your goals.</p>
    <p class="offer">As a way to give back to my community, I am offering new clients six free coaching sessions. This is a limited time offer.</p>
    <p class="quote">Please contact me. I’m ready to support you as you work to improve your health. - Jen Talvora</p>
  </div>

  <svg class="foot-curve" viewBox="0 0 480 120" preserveAspectRatio="none" aria-hidden="true">
    <path d="M0 52 Q240 20 480 52 L480 120 L0 120Z" fill="var(--swoosh-grey)"/>
    <path d="M0 60 Q240 30 480 60 L480 120 L0 120Z" fill="var(--white)"/>
  </svg>
  <div class="phone">
    <svg viewBox="0 0 20 20" aria-hidden="true"><circle cx="10" cy="10" r="8.5" fill="none" stroke="currentColor" stroke-width="1.5"/><path d="M7 5.5c.6-.3 1 0 1.3.6l.6 1.3c.2.5 0 .9-.4 1.2l-.4.3c.4 1 1.2 1.8 2.2 2.3l.3-.4c.3-.4.8-.6 1.2-.4l1.3.6c.6.3.8.8.5 1.3-.5 1-1.5 1.4-2.6 1-2.2-.8-3.9-2.5-4.7-4.7-.4-1.1 0-2.2.7-2.9z" fill="currentColor"/></svg>
    <span>555-210-4837</span>
  </div>
  <p class="contact">Please contact Jen Talvora: talvorahwc@mailbox.example</p>
</section>

</body>
</html>
```